CoinLantern one-page corporate website

Our company, CoinLantern is a cryptocurrency Initial Coin Offering ("ICO" marketing and promotion agency, which requires a professional company landing page design whereby prospective clients can learn;
-who we are
-what we do
-what our people are saying about us
-core team members
-subscribe to our mailing list
-how to get in touch (basic contact form)

We are looking for something unique and attractive -- not a standard Pako template that we could put together ourselves. Plain stock images should not be used. Unique visualizations of the service offerings and creative presentation are key. We are a cutting edge marketing agency and as such, we need to look the part.

Relevant documentation about the business and branding assets have been attached to guide the designer. Certain information will be included by the company at a later date such as team member descriptions. As such, lorem ipsum may be included wherever necessary to help visualize the textual areas.

****Please ensure that you actually utilize the photos and graphics provided so that we can have a good picture of what it would actually look like with our branding.

The site must be responsive HTML CSS Design.

Sites style themes we like for inspiration and specific sections we like ****Very important***:
https://vaultorbitra.example/offers - we like that the token & company logo is used in unique visualizations that connects various ideas together. We imagine unique visuals such as these with our Icon (see attached) serving as a token. We also like the unique and attractive visual theme of the webpage itself.

https://quarrelstone.example/ - we like the layout of this website, specifically how the service offerings are displayed in a circular visual graphic with the Quarrel logo in the middle. We imagine a similar type of graphic designed with CoinLantern in the middle.

https://zorvinet.example/ - we like how the logo is central to the theme in this site when you first enter and how it fades + shrinks into the distance as you scroll down.

Target Market(s)

cryptocurrency entrepreneurs and ICOs

Industry/Entity Type

It Company

Coding

Coded - Design and coding required

Number of Pages Required

1 page

Font styles to use
Sans Serif

Colors

Designer to choose colors to be used in the design.

Requirements
Must have
• The site must be responsive HTML CSS Design.
• The page must be modern and visually attractive. Elements must not be static and should have a fluid motion / visual change as the user scrolls through the page.
Should not have
• The project should not use any old stock images or elements which are dull and over-used, but rather images or elements should be unique and well thought out.

```html
<!DOCTYPE html>
<html lang="en">
<head>
<meta charset="utf-8">
<title>CoinLantern — The Token Sale Experts</title>
<link href="https://fonts.googleapis.com/css2?family=Montserrat:wght@400;500;600;700;800&family=Open+Sans:wght@400;600&display=swap" rel="stylesheet">
<style>
:root{
  --hero-top:#0d63b4;
  --hero-mid:#1f8fe3;
  --hero-light:#55b6f2;
  --navy:#152f4f;
  --navy-deep:#0f2540;
  --accent:#1b8fe6;
  --accent-dark:#0f6fc0;
  --ink:#2d3c4e;
  --muted:#6b7785;
  --line:#d9e3ec;
  --white:#ffffff;
  --sky-top:#8fb3cf;
  --sky-low:#e9f0f6;
}
*{box-sizing:border-box;margin:0;padding:0}
html,body{width:1200px;height:4009px;overflow:hidden}
body{position:relative;background:var(--white);font-family:"Open Sans",Arial,sans-serif;color:var(--ink)}
.abs{position:absolute}
h1,h2,h3,h4,.heading{font-family:"Montserrat",Arial,sans-serif}

/* HERO */
.hero{left:0;top:0;width:1200px;height:716px;background:radial-gradient(ellipse at 75% 30%,var(--hero-light) 0%,var(--hero-mid) 40%,var(--hero-top) 100%);overflow:hidden;color:var(--white)}
.hero-waves{left:0;top:0}
.social{right:40px;top:40px;display:flex;gap:8px}
.social span{width:22px;height:22px;border-radius:50%;background:var(--white)}
.menu-toggle{left:50px;top:356px;width:34px}
.menu-toggle i{display:block;height:3px;background:var(--white);margin-bottom:8px}
.menu-toggle i:nth-child(2){width:24px}
.brand-mark{left:530px;top:60px;width:140px;height:140px;border:6px solid var(--white);border-radius:50%}
.brand-name{left:0;width:1200px;top:348px;text-align:center;font-family:"Montserrat",sans-serif;font-weight:600;font-size:72px;letter-spacing:3px;line-height:1}
.brand-tag{left:0;width:1200px;top:428px;text-align:center;font-family:"Montserrat",sans-serif;font-weight:600;font-size:26px}
.hero-copy{left:210px;width:780px;top:484px;text-align:center;font-size:16px;line-height:26px}
.btn-start{left:510px;top:573px;width:180px;height:42px;border-radius:21px;background:var(--white);color:var(--accent-dark);font-family:"Montserrat",sans-serif;font-size:13px;font-weight:500;display:flex;align-items:center;justify-content:center;letter-spacing:.5px}
.scroll-mouse{left:590px;top:655px;width:18px;height:30px;border:2px solid var(--white);border-radius:9px}
.scroll-mouse::after{content:"";position:absolute;left:6px;top:5px;width:2px;height:7px;background:var(--white)}

/* NAV */
.main-nav{left:0;top:716px;width:1200px;height:91px;background:var(--white);border-bottom:1px solid var(--line)}
.nav-group{top:0;height:91px;display:flex;align-items:center;gap:34px;font-family:"Montserrat",sans-serif;font-size:14px;color:var(--ink)}
.nav-left{left:160px}
.nav-right{left:682px}
.nav-left a:first-child{border-bottom:2px solid var(--accent);padding-bottom:3px}
.nav-mark{left:574px;top:18px;width:54px;height:54px;border-radius:50%;border:3px solid var(--accent);background:var(--white);box-shadow:0 2px 8px rgba(0,0,0,.12)}

/* WHO WE ARE */
.who-visual{left:13px;top:818px;width:575px;height:460px;background:linear-gradient(180deg,#f4f8fc 0%,#e3edf7 100%);border:1px solid var(--line)}
.who-text{left:647px;top:858px;width:430px}
.kicker{font-family:"Montserrat",sans-serif;font-size:14px;color:var(--ink);letter-spacing:.5px}
.who-text h2{font-size:30px;font-weight:800;color:var(--accent);margin:2px 0 22px;position:relative}
.who-text h2::before{content:"";position:absolute;left:0;top:-4px;width:440px;height:1px;background:var(--line)}
.who-text p{font-size:13.5px;line-height:21px;color:var(--muted);margin-bottom:22px}

/* WHAT WE DO */
.what{left:0;top:1288px;width:1200px;height:743px;background:var(--navy)}
.title-box{height:61px;border:3px solid var(--white);display:flex;align-items:center;justify-content:center;font-family:"Montserrat",sans-serif;font-weight:700;font-size:29px;letter-spacing:1px}
.title-mark{width:40px;height:40px;border-radius:50%;border:3px solid currentColor;background:inherit}
.what .title-box{left:473px;top:67px;width:251px;color:var(--white)}
.what .title-mark{left:579px;top:48px;color:var(--white);background:var(--navy)}
.what-intro{left:120px;width:960px;top:160px;text-align:center;color:var(--white);font-size:13.5px;line-height:20px}
.service-list{top:256px;list-style:none;color:var(--white);font-size:14.5px}
.service-list li{position:relative;height:56px;padding-left:46px;line-height:20px;display:flex;align-items:center}
.service-list li.two{height:62px}
.service-list svg{position:absolute;left:0;top:50%;margin-top:-15px}
.col-left{left:147px;width:400px}
.col-right{left:663px;width:440px}
.down-tab{left:560px;top:701px;width:80px;height:42px;background:var(--sky-low);border-radius:40px 40px 0 0}

/* ABOUT */
.about{left:0;top:2031px;width:1200px;height:481px;overflow:hidden}
.about-sky{left:0;top:0;width:1200px;height:481px;background:linear-gradient(180deg,var(--sky-low) 0%,#f6f9fc 45%,#b9cddd 75%,var(--sky-top) 100%)}
.about .title-box{left:473px;top:50px;width:252px;color:var(--accent);border-color:var(--accent);background:rgba(255,255,255,.6)}
.about .title-mark{left:580px;top:31px;color:var(--accent);background:var(--white)}
.about h3{left:0;width:1200px;top:134px;text-align:center;font-size:20px;font-weight:700;color:var(--navy)}
.about-copy{left:152px;width:896px;top:176px;text-align:center;font-size:13.5px;line-height:21px;color:var(--ink)}
.about-copy p{margin-bottom:21px}

/* TEAM */
.team{left:0;top:2512px;width:1200px;height:620px;background:linear-gradient(180deg,#ffffff 0%,#eef3f8 100%)}
.team .title-box{left:408px;top:70px;width:384px;color:var(--accent);border-color:var(--accent);background:var(--white);font-size:27px}
.team .title-mark{left:580px;top:50px;color:var(--accent);background:var(--white)}
.member{top:179px;width:316px;height:462px;background:var(--white);box-shadow:0 6px 20px rgba(20,40,70,.15)}
.member .photo{position:absolute;left:0;top:0;width:316px;height:296px}
.m1{left:102px}.m3{left:788px}
.m1 .photo{background:linear-gradient(160deg,#c9b59c 0%,#8a6a52 55%,#5b4636 100%)}
.m3 .photo{background:linear-gradient(160deg,#9a9a9a 0%,#555 60%,#2c2c2c 100%)}
.member h4{position:absolute;left:0;width:100%;top:338px;text-align:center;font-size:26px;font-weight:700;color:var(--navy)}
.member .role{position:absolute;left:0;width:100%;top:374px;text-align:center;font-family:"Montserrat",sans-serif;font-size:10px;letter-spacing:1px;color:var(--muted)}
.member .links{position:absolute;left:0;width:100%;top:398px;display:flex;justify-content:center;gap:8px}
.member .links span{width:26px;height:26px;border-radius:50%;background:var(--accent)}
.m2{left:444px;top:179px;width:318px;height:462px;background:var(--navy-deep);color:var(--white)}
.m2::before{content:"";position:absolute;left:20px;top:20px;right:20px;bottom:20px;border:1px solid rgba(255,255,255,.3)}
.m2 h4{position:absolute;left:0;width:100%;top:66px;text-align:center;font-size:25px;font-weight:700}
.m2 .role{position:absolute;left:0;width:100%;top:100px;text-align:center;font-family:"Montserrat",sans-serif;font-size:10px;letter-spacing:1px;color:#c9d6e4}
.m2 p{position:absolute;left:50px;width:218px;top:130px;text-align:center;font-size:12px;line-height:19px}
.m2 .links{position:absolute;left:0;width:100%;top:398px;display:flex;justify-content:center;gap:8px}
.m2 .links span{width:26px;height:26px;border-radius:50%;background:var(--accent)}

/* MAILING */
.mailing{left:0;top:3132px;width:1200px;height:208px;background:var(--navy-deep);overflow:hidden;z-index:2}
.mailing svg{position:absolute;left:0;top:0}
.mail-mark{left:92px;top:56px;width:94px;height:94px;border-radius:50%;border:4px solid var(--white)}
.mail-kicker{left:210px;top:66px;font-family:"Montserrat",sans-serif;font-size:30px;color:var(--white);letter-spacing:1px}
.mail-title{left:210px;top:116px;font-family:"Montserrat",sans-serif;font-size:66px;font-weight:800;color:var(--accent);line-height:1}
.btn-subscribe{left:945px;top:128px;width:160px;height:44px;border:2px solid var(--white);color:var(--white);font-family:"Montserrat",sans-serif;font-size:14px;display:flex;align-items:center;justify-content:center;letter-spacing:1px}

/* CONTACT */
.contact{left:0;top:3340px;width:1200px;height:615px;background:linear-gradient(135deg,#1a93e6 0%,#1379cf 45%,#0c4f93 100%)}
.contact .title-box{left:445px;top:105px;width:310px;color:var(--white);border-color:var(--white)}
.contact .title-mark{left:580px;top:86px;color:var(--white);background:#1585d9}
.rule{top:136px;height:1px;width:240px;background:rgba(255,255,255,.5)}
.field{height:40px;border:1px solid rgba(255,255,255,.85);color:var(--white);font-size:11px;padding:0 14px;display:flex;align-items:center;letter-spacing:.5px}
.f-a{left:214px;width:374px}.f-b{left:620px;width:369px}
.r1{top:232px}.r2{top:302px}
.f-msg{left:214px;top:350px;width:775px;height:126px;align-items:flex-start;padding-top:10px}
.btn-send{left:214px;top:502px;width:775px;height:38px;background:var(--white);color:var(--navy);font-family:"Montserrat",sans-serif;font-weight:600;font-size:14px;display:flex;align-items:center;justify-content:center;letter-spacing:1px}
.foot-chev{left:588px;top:578px}

/* FOOTER */
.site-footer{left:0;top:3955px;width:1200px;height:54px;background:var(--navy-deep);color:var(--white);font-family:"Montserrat",sans-serif;font-size:13px;letter-spacing:1px;display:flex;align-items:center;justify-content:center}
</style>
</head>
<body>

<header class="hero abs">
  <svg class="hero-waves abs" width="1200" height="716" viewBox="0 0 1200 716" fill="none" stroke="rgba(255,255,255,.18)" stroke-width="1.5">
    <path d="M-20 520 C 250 420, 500 640, 800 480 S 1150 300, 1230 380"/>
    <path d="M-20 560 C 260 460, 520 660, 820 510 S 1150 340, 1230 420"/>
    <path d="M-20 600 C 280 500, 540 690, 840 540 S 1150 380, 1230 460"/>
    <path d="M700 -10 C 820 120, 960 60, 1210 180"/>
  </svg>
  <div class="social abs"><span></span><span></span><span></span></div>
  <div class="menu-toggle abs" aria-label="Menu"><i></i><i></i><i></i></div>
  <div class="brand-mark abs"></div>
  <h1 class="brand-name abs">COINLANTERN</h1>
  <div class="brand-tag abs">The Token Sale Experts</div>
  <p class="hero-copy abs">CoinLantern is the premier marketing agency for ICO's. Our experts will ensure that your ICO is run properly, communicated well, and achieves your desired outcomes.</p>
  <a class="btn-start abs">GET STARTED</a>
  <div class="scroll-mouse abs"></div>
</header>

<nav class="main-nav abs">
  <div class="nav-group nav-left abs"><a>WHO WE ARE</a><a>WHAT WE DO</a><a>ABOUT US</a></div>
  <div class="nav-mark abs"></div>
  <div class="nav-group nav-right abs"><a>TEAM MEMBERS</a><a>SUBSCRIBE</a><a>GET IN TOUCH</a></div>
</nav>

<section class="who">
  <div class="who-visual abs" role="img" aria-label="Illustration of the CoinLantern token connected to team, coin stack and service badges"></div>
  <div class="who-text abs">
    <div class="kicker">WHO WE ARE</div>
    <h2>WHO ARE YOU?</h2>
    <p>We are a group of global experts connected through a cutting edge Decentralized Organizational structure powered by Smart Contracts. We have no employees – just owners. That is why your success is our shared mission.</p>
    <h2>HOW MUCH DOES IT COST?</h2>
    <p>Every Token sale is unique, that is why CoinLantern begins with a one-on-one conversation to identify your specific needs and agree upon terms that make sense for all parties. We structure engagements according to the principle of aligned interests - our success is your success and vice versa.</p>
  </div>
</section>

<section class="what abs">
  <div class="title-box abs">WHAT WE DO</div>
  <div class="title-mark abs"></div>
  <p class="what-intro abs">We will work with you from ensuring your whitepaper properly communicates your vision through ensuring the security of the last token sold in the ICO. We will do this by employing our assets to ensure that your interests are secured all the way through the sale. The means to accomplish your successful token sale will be done using some or all of the following:</p>
  <ul class="service-list col-left abs">
    <li><svg width="30" height="30" viewBox="0 0 30 30" fill="none" stroke="#fff" stroke-width="1.6"><circle cx="15" cy="15" r="13"/><path d="M10 8h8l3 3v11H10z"/></svg>Whitepaper Consultation and Review</li>
    <li class="two"><svg width="30" height="30" viewBox="0 0 30 30" fill="none" stroke="#fff" stroke-width="1.6"><circle cx="15" cy="15" r="13"/><path d="M8 18l5-5 4 4 5-6"/></svg>Connections to the best legal and<br>accounting practices depending on your situation</li>
    <li><svg width="30" height="30" viewBox="0 0 30 30" fill="none" stroke="#fff" stroke-width="1.6"><circle cx="15" cy="15" r="13"/><circle cx="15" cy="15" r="6"/></svg>Token sale strategy</li>
    <li><svg width="30" height="30" viewBox="0 0 30 30" fill="none" stroke="#fff" stroke-width="1.6"><circle cx="15" cy="15" r="13"/><path d="M9 20l4-5 3 3 5-7"/></svg>Raise amount and future token price strategy</li>
    <li><svg width="30" height="30" viewBox="0 0 30 30" fill="none" stroke="#fff" stroke-width="1.6"><circle cx="15" cy="15" r="13"/><circle cx="15" cy="12" r="3.5"/><path d="M9 22c1-4 11-4 12 0"/></svg>KYC (Know Your Customer) strategies</li>
    <li><svg width="30" height="30" viewBox="0 0 30 30" fill="none" stroke="#fff" stroke-width="1.6"><circle cx="15" cy="15" r="13"/><rect x="10" y="14" width="10" height="8"/><path d="M12 14v-3a3 3 0 0 1 6 0v3"/></svg>Secure Token Launch Website</li>
    <li><svg width="30" height="30" viewBox="0 0 30 30" fill="none" stroke="#fff" stroke-width="1.6"><circle cx="15" cy="15" r="13"/><path d="M9 13v4h3l6 4V9l-6 4z"/></svg>Marketing Representation</li>
    <li><svg width="30" height="30" viewBox="0 0 30 30" fill="none" stroke="#fff" stroke-width="1.6"><circle cx="15" cy="15" r="13"/><path d="M9 10h12v8h-7l-4 3v-3H9z"/></svg>Social Media management</li>
  </ul>
  <ul class="service-list col-right abs">
    <li><svg width="30" height="30" viewBox="0 0 30 30" fill="none" stroke="#fff" stroke-width="1.6"><circle cx="15" cy="15" r="13"/><rect x="9" y="10" width="12" height="10"/><path d="M11 13h8M11 16h8"/></svg>News and Press related strategies and execution</li>
    <li class="two"><svg width="30" height="30" viewBox="0 0 30 30" fill="none" stroke="#fff" stroke-width="1.6"><circle cx="15" cy="15" r="13"/><path d="M9 11h12M9 15h12M9 19h8"/></svg>Multi-language translation and promotion</li>
    <li><svg width="30" height="30" viewBox="0 0 30 30" fill="none" stroke="#fff" stroke-width="1.6"><circle cx="15" cy="15" r="13"/><circle cx="12" cy="13" r="3"/><circle cx="19" cy="13" r="3"/><path d="M7 21c1-3 9-3 10 0"/></svg>Access to our proprietary list of investors</li>
    <li><svg width="30" height="30" viewBox="0 0 30 30" fill="none" stroke="#fff" stroke-width="1.6"><circle cx="15" cy="15" r="13"/><path d="M8 15l4 4 10-9"/></svg>Public Relations</li>
    <li><svg width="30" height="30" viewBox="0 0 30 30" fill="none" stroke="#fff" stroke-width="1.6"><circle cx="15" cy="15" r="13"/><circle cx="15" cy="11" r="2.5"/><circle cx="10" cy="19" r="2.5"/><circle cx="20" cy="19" r="2.5"/></svg>Community Development &amp; Management</li>
    <li><svg width="30" height="30" viewBox="0 0 30 30" fill="none" stroke="#fff" stroke-width="1.6"><circle cx="15" cy="15" r="13"/><path d="M15 8l2 5h5l-4 3 2 5-5-3-5 3 2-5-4-3h5z"/></svg>Bounty program development and management</li>
    <li><svg width="30" height="30" viewBox="0 0 30 30" fill="none" stroke="#fff" stroke-width="1.6"><circle cx="15" cy="15" r="13"/><path d="M10 20V12h3v8M16 20V9h3v11"/></svg>High-touch individual sales for larger buyers</li>
    <li><svg width="30" height="30" viewBox="0 0 30 30" fill="none" stroke="#fff" stroke-width="1.6"><circle cx="15" cy="15" r="13"/><path d="M15 22V12M15 14c-4 0-6-3-6-6 4 0 6 3 6 6zM15 16c3 0 6-2 6-6-4 0-6 2-6 6z"/></svg>Organic grassroots promotion</li>
  </ul>
  <div class="down-tab abs"><svg width="80" height="42" viewBox="0 0 80 42" fill="none" stroke="#152f4f" stroke-width="2.5"><path d="M33 20l7 7 7-7"/></svg></div>
</section>

<section class="about abs">
  <div class="about-sky abs" role="img" aria-label="Sky scene with clouds above mountain peaks"></div>
  <div class="title-box abs">ABOUT US</div>
  <div class="title-mark abs"></div>
  <h3 class="abs">HOW DOES IT WORK?</h3>
  <div class="about-copy abs">
    <p>Our tight-knit group of experts becomes a part of your team for the crucial period leading up to and during your ICO. We take the time to thoroughly understand your project and the people behind it. By drawing on our deep expertise in the space and network of valuable connections, we work closely with you to develop and implement the steps involved in executing a successful ICO. Best practices, market conditions, and investor psychology are constantly changing. We stay laser-focused on the ICO segment of the cryptocurrency landscape to stay up to date.</p>
    <p>Bringing CoinLantern in to run your sale allows your team members to focus on execution. Without the hassle, distraction, and frustration of trying to do it yourself, you have more bandwidth to build out your vision.</p>
  </div>
</section>

<section class="team abs">
  <div class="title-box abs">CORE TEAM MEMBERS</div>
  <div class="title-mark abs"></div>
  <article class="member m1 abs">
    <div class="photo" role="img" aria-label="Portrait photo of the founder"></div>
    <h4>DALEN VOSS</h4>
    <div class="role">FOUNDER / CEO</div>
    <div class="links"><span></span><span></span></div>
  </article>
  <article class="m2 abs">
    <h4>MIRO TALLIS</h4>
    <div class="role">CREATIVE DIRECTOR</div>
    <p>Lorem Ipsum is simply dummy text of the printing and typesetting industry. Lorem Ipsum has been the industry's standard dummy text ever since the 1500s, when an unknown printer took a galley of type and scrambled it to make a type specimen book. It has survived not only five centuries, but also the leap into electronic typesetting, remaining essentially unchanged.</p>
    <div class="links"><span></span><span></span></div>
  </article>
  <article class="member m3 abs">
    <div class="photo" role="img" aria-label="Black and white portrait photo of the development lead"></div>
    <h4>OREN KASTEL</h4>
    <div class="role">DEVELOPMENT LEAD</div>
    <div class="links"><span></span><span></span></div>
  </article>
</section>

<section class="mailing abs">
  <svg width="1200" height="208" viewBox="0 0 1200 208">
    <polygon points="860,0 1200,0 1200,208 760,208" fill="#163a63"/>
    <polygon points="880,0 920,0 830,208 790,208" fill="#1b8fe6"/>
    <polygon points="1130,0 1200,0 1200,208 1050,208" fill="#1b8fe6" opacity=".55"/>
    <rect x="0" y="0" width="1200" height="8" fill="#1b8fe6"/>
  </svg>
  <div class="mail-mark abs"></div>
  <div class="mail-kicker abs">SUBSCRIBE TO OUR</div>
  <div class="mail-title abs">MAILING LIST</div>
  <a class="btn-subscribe abs">SUBSCRIBE</a>
</section>

<section class="contact abs">
  <div class="rule abs" style="left:190px"></div>
  <div class="rule abs" style="left:770px"></div>
  <div class="title-box abs">GET IN TOUCH</div>
  <div class="title-mark abs"></div>
  <div class="field f-a r1 abs">FIRST NAME*</div>
  <div class="field f-b r1 abs">LAST NAME*</div>
  <div class="field f-a r2 abs">E-MAIL ADDRESS*</div>
  <div class="field f-b r2 abs">PHONE NUMBER*</div>
  <div class="field f-msg abs">MESSAGE</div>
  <a class="btn-send abs">SEND NOW</a>
  <svg class="foot-chev abs" width="24" height="16" viewBox="0 0 24 16" fill="none" stroke="#fff" stroke-width="2.5"><path d="M4 4l8 8 8-8"/></svg>
</section>

<footer class="site-footer abs">©2017 COINLANTERN | ALL RIGHTS RESERVED</footer>

</body>
</html>
```